Create a capturing book cover for The Hollow Lantern

Book Title: The Hollow Lantern
Subtitle: Finding Quiet Beyond the Harbor
Author: Marisole Dunphrey

Synopsis of book:
She didn’t really know what she wanted to do, but she knew she wanted to be successful. She struggled with identifying with what she was passionate about and what her purpose was for her life. Fear, turmoil, relationships, and career paths created turbulence in her long journey to fulfill her vision and lifetime goals. The Hollow Lantern exemplifies women who struggle with these things. The Hollow Lantern digs into the crevices of a blurry vision, disturbed, and fearful woman.

-The book focuses on a woman who is not necessarily physically cripple, but mentally, spiritually, and emotionally crippled.

The photos attached are just examples (not all have to be used)

Target Market(s)

Women who are dealing with barriers that are holding them back from reaching their goals or being successful

Font styles to use
Serif
Sans Serif

Colors
6b449b
b7a5cd

Requirements
Must have
• purple incorporated (not the full cover)
• I would like an African American woman, dominican woman, or mixed (you cannot tell what ethnicity she is) on the front cover if any.
Nice to have
• I would like the cover to tell the story. My ideas were maybe an actual crippled woman looking into the mirror at a woman who is at peace, or two women in one that shows one struggling and one living in happiness, or a crippled woman with her back turned and a path with something that symbolizes happiness at the end, or a lady sitting on the floor kind of distraught. I really want the designer to be creative. I do not have an exact image of what I want it to look like. These are just ideas. They do not have to be within the realms that I mentioned.
Should not have
• Extravagant text
• cartoon or animated pictures
• do not want a dark cover

```html
<!DOCTYPE html>
<html lang="en">
<head>
<meta charset="utf-8">
<title>The Hollow Lantern — Cover Spread</title>
<link href="https://fonts.googleapis.com/css2?family=Josefin+Sans:wght@300;400&family=Great+Vibes&display=swap" rel="stylesheet">
<style>
  :root {
    --page: #ffffff;
    --purple-deep: #4a1f63;
    --purple: #6b449b;
    --purple-mid: #8a64ad;
    --lavender: #b7a5cd;
    --mist: #efe9f4;
    --ink: #3a1a4f;
    --script-ink: #2a0f3a;
  }
  html, body {
    margin: 0;
    width: 1200px;
    height: 1000px;
    overflow: hidden;
    background: var(--page);
  }
  .spread { position: relative; width: 1200px; height: 1000px; }

  .panel {
    position: absolute;
    box-shadow: 2px 3px 5px rgba(0,0,0,0.35);
    overflow: hidden;
  }
  .back-cover  { left: 156px; top: 135px; width: 442px; height: 693px; }
  .spine       { left: 610px; top: 155px; width: 30px;  height: 695px; }
  .front-cover { left: 653px; top: 135px; width: 437px; height: 695px; }

  .back-cover .artwork {
    position: absolute; inset: 0;
    background:
      radial-gradient(ellipse 40% 30% at 85% 70%, var(--purple-deep) 0 60%, transparent 100%),
      linear-gradient(160deg, var(--purple-mid), var(--purple-deep));
  }
  .back-cover .veil {
    position: absolute; left: 42px; top: 40px; width: 400px; height: 620px;
    background:
      radial-gradient(ellipse 30% 40% at 98% 70%, rgba(74,31,99,0.95) 0 55%, transparent 100%),
      linear-gradient(175deg, var(--mist) 0%, #e4d9ec 45%, var(--lavender) 100%);
  }
  .front-cover .artwork {
    position: absolute; inset: 0;
    background:
      radial-gradient(ellipse 30% 20% at 20% 8%, var(--mist) 0 50%, transparent 100%),
      linear-gradient(200deg, var(--purple-mid), var(--purple-deep) 60%);
  }
  .front-cover .veil {
    position: absolute; left: 0; top: 40px; width: 395px; height: 620px;
    background:
      radial-gradient(ellipse 45% 25% at 40% 32%, rgba(255,255,255,0.9) 0 45%, transparent 100%),
      radial-gradient(ellipse 60% 55% at 65% 75%, var(--purple-deep) 0 55%, transparent 100%),
      linear-gradient(170deg, #d9cce6 0%, var(--lavender) 35%, var(--purple) 70%, var(--purple-deep) 100%);
  }
  .spine .artwork {
    position: absolute; inset: 0;
    background: linear-gradient(180deg, var(--mist) 0%, var(--lavender) 25%, var(--purple) 55%, var(--purple-deep) 100%);
  }

  .synopsis {
    position: absolute; left: 50px; top: 150px; width: 390px;
    margin: 0;
    font-family: "Josefin Sans", sans-serif;
    font-weight: 400;
    font-size: 16px;
    line-height: 20px;
    font-variant: small-caps;
    letter-spacing: 0.6px;
    color: var(--ink);
    text-align: center;
  }

  .spine-title {
    position: absolute; left: 3px; top: 18px;
    writing-mode: vertical-rl;
    font-family: "Great Vibes", cursive;
    font-size: 20px;
    color: var(--script-ink);
    white-space: nowrap;
  }
  .spine-author {
    position: absolute; left: 5px; top: 460px;
    writing-mode: vertical-rl;
    font-family: "Josefin Sans", sans-serif;
    font-weight: 300;
    font-size: 16px;
    letter-spacing: 1px;
    text-transform: uppercase;
    color: #f4eef8;
    white-space: nowrap;
  }

  .cover-title {
    position: absolute; left: 40px; top: 150px; margin: 0;
    font-family: "Great Vibes", cursive;
    font-weight: 400;
    color: var(--script-ink);
    line-height: 1;
  }
  .cover-title .article { display: block; font-size: 26px; margin-left: 6px; }
  .cover-title .main { display: block; font-size: 50px; margin-top: -10px; }
  .cover-subtitle {
    position: absolute; left: 70px; top: 248px; margin: 0;
    font-family: "Great Vibes", cursive;
    font-size: 28px;
    color: #ffffff;
    -webkit-text-stroke: 0.6px var(--purple-deep);
    line-height: 1;
    text-align: center;
  }
  .cover-subtitle .small { font-size: 15px; }
  .cover-author {
    position: absolute; left: 0; top: 615px; width: 395px;
    font-family: "Josefin Sans", sans-serif;
    font-weight: 300;
    font-size: 31px;
    letter-spacing: 1px;
    text-transform: uppercase;
    text-align: center;
    color: #ffffff;
    white-space: nowrap;
  }
</style>
</head>
<body>
<main class="spread">
  <section class="panel back-cover">
    <div class="artwork" role="img" aria-label="Purple-toned photograph of bare winter branches framing the back cover"></div>
    <div class="veil" role="img" aria-label="Faded rain-streaked photograph of a woman's profile in lavender tones"></div>
    <p class="synopsis">She didn't really know what she wanted to do, but she knew she wanted to be successful. She struggled with identifying with what she was passionate about and what her purpose was for her life. Fear, turmoil, relationships, and career paths created turbulence in her long journey to fulfill her vision and lifetime goals. The Hollow Lantern exemplifies women who struggle with these things. The Hollow Lantern digs into the crevices of a blurry vision, disturbed, and fearful woman.</p>
  </section>

  <section class="panel spine">
    <div class="artwork" role="img" aria-label="Spine continuation of the purple photograph"></div>
    <span class="spine-title">The Hollow Lantern</span>
    <span class="spine-author">Marisole Dunphrey</span>
  </section>

  <section class="panel front-cover">
    <div class="artwork" role="img" aria-label="Purple-toned photograph with bare branches across the front cover"></div>
    <div class="veil" role="img" aria-label="Rain-blurred photograph of a woman in shadow, washed in purple and lavender"></div>
    <h1 class="cover-title"><span class="article">The</span><span class="main">Hollow Lantern</span></h1>
    <p class="cover-subtitle">Finding Quiet Beyond<br><span class="small">the</span> Harbor</p>
    <div class="cover-author">Marisole Dunphrey</div>
  </section>
</main>
</body>
</html>
```